Business Card Design

We are a flooring/granite/cabinet company
want a sleek and modern design card. Will send our logo. maybe our logo in 3d on card.
black card

Industry/Entity Type

Business

Contact Information for Business Card

Gregory Tallis
company name Stone Hearth Depot
4827 fm 71s 78540
210-634-8872
stonehearthdepot@mailvista.example

```html
<!DOCTYPE html>
<html lang="en">
<head>
<meta charset="utf-8">
<title>Stone Hearth Depot — Business Card</title>
<link rel="stylesheet" href="https://fonts.googleapis.com/css2?family=Roboto:wght@300;400;700&family=Michroma&display=swap">
<style>
  :root {
    --backdrop: #e9e6e1;
    --card-dark: #1d2330;
    --card-dark-deep: #131823;
    --card-speck: #2b3344;
    --panel-white: #f7f7f7;
    --ink-light: #ffffff;
    --ink-soft: #dfe3ea;
    --brand-blue: #1f5f8b;
  }
  * { margin: 0; padding: 0; box-sizing: border-box; }
  html, body {
    width: 1200px; height: 1000px; overflow: hidden;
    background: var(--backdrop);
  }
  .stage {
    position: relative; width: 1200px; height: 1000px;
  }
  .card {
    position: absolute; left: 280px; width: 640px; height: 366px;
    border-radius: 6px; overflow: hidden;
    background: radial-gradient(ellipse at 30% 20%, var(--card-speck) 0%, var(--card-dark) 45%, var(--card-dark-deep) 100%);
    box-shadow: 0 10px 28px rgba(0,0,0,0.25);
  }
  .card--front { top: 100px; }
  .card--back { top: 534px; }

  .front__panel {
    position: absolute; left: 0; bottom: 0; width: 270px; height: 220px;
    background: var(--panel-white);
    border-top-right-radius: 34px;
    display: flex; align-items: center; justify-content: center;
  }
  .front__brand {
    font-family: "Michroma", sans-serif; font-size: 17px; color: var(--brand-blue);
    display: flex; align-items: center; gap: 10px; letter-spacing: 0.5px;
  }
  .brand-square { width: 14px; height: 14px; background: currentColor; }

  .front__name {
    position: absolute; right: 40px; top: 36px;
    font-family: "Roboto", sans-serif; font-weight: 700; font-size: 30px;
    color: var(--ink-light); letter-spacing: 0.5px;
  }
  .front__rule {
    position: absolute; left: 262px; right: 40px; top: 84px;
    height: 2px; background: var(--ink-light);
  }
  .front__contact {
    position: absolute; right: 40px; top: 112px; text-align: right;
    font-family: "Roboto", sans-serif; font-weight: 300; font-size: 21px;
    line-height: 30px; color: var(--ink-soft);
  }
  .front__email {
    position: absolute; right: 40px; bottom: 34px;
    font-family: "Roboto", sans-serif; font-weight: 300; font-size: 19px;
    color: var(--ink-soft);
  }

  .back__brand {
    position: absolute; inset: 0;
    display: flex; align-items: center; justify-content: center; gap: 16px;
    font-family: "Michroma", sans-serif; font-size: 34px; color: var(--ink-light);
    letter-spacing: 1px;
  }
  .back__brand .brand-square { width: 24px; height: 24px; }
</style>
</head>
<body>
  <main class="stage">
    <section class="card card--front" aria-label="Business card front">
      <div class="front__panel">
        <div class="front__brand"><span class="brand-square"></span>Stone Hearth Depot</div>
      </div>
      <h1 class="front__name">Gregory Tallis</h1>
      <div class="front__rule"></div>
      <address class="front__contact">
        4827 fm 71s 78540<br>
        210-634-8872
      </address>
      <div class="front__email">stonehearthdepot@mailvista.example</div>
    </section>

    <section class="card card--back" aria-label="Business card back">
      <div class="back__brand"><span class="brand-square"></span>Stone Hearth Depot</div>
    </section>
  </main>
</body>
</html>
```